Envelope design

We need a envelope design for a professional services firm called Brindlemoor Tax Consultancy Inc. The firm is essentially a very specialized tax accounting firm - instead of serving the end consumer, we support other public accounting firms in the area of Canadian and U.S. tax advisory and compliance (i.e. they call us on tax issues too complex for the general practitioner). Our byline is "Tax Support Services for Public Accounting Firms". Our postcard should utilize our logo and be based on colours present in our logo (see file attached). The final design needs to convey professionalism and trustworthiness (we're hired by accountants after all!) while being creative and eye-catching. Eye-catching is critical, since many prospective recipients will not have heard from me before and I want them to read the postcard.
At lot of design work has already been done here. I've attached a number of sample files showing logo and letterhead designs. Please note that the letterhead hasn't yet been updated for the new logo. This is happening in a separate design competition.
Updates
Project Deadline Extended Reason: Deadline is extended because I am pricing the extra cost of having colour right to the edge of the envelopes. This will help me design on final design. Pricing should come in on Monday. Added Saturday, February 20, 2016

```html
<!DOCTYPE html>
<html lang="en">
<head>
<meta charset="utf-8">
<title>Brindlemoor Tax Consultancy – Envelope Options</title>
<link rel="stylesheet" href="https://fonts.googleapis.com/css2?family=Source+Sans+3:wght@400;600&display=swap">
<style>
  :root {
    --board: #333333;
    --paper: #ffffff;
    --ink: #1a1a1a;
    --grey: #7a7a7a;
    --navy: #1b3060;
    --orange: #e8523a;
    --amber: #f2a330;
    --sky: #1e95d2;
    --label: #ffffff;
  }
  * { box-sizing: border-box; margin: 0; padding: 0; }
  html, body { width: 1200px; height: 1164px; overflow: hidden; }
  body { background: var(--board); position: relative; font-family: "Source Sans 3", Arial, sans-serif; }

  .option-number {
    position: absolute; left: 36px;
    font: 600 44px "Source Sans 3", Arial, sans-serif; color: var(--label);
  }

  .envelope {
    position: absolute; left: 94px; width: 1065px; height: 464px;
    background: var(--paper); overflow: hidden;
    box-shadow: 0 6px 14px rgba(0,0,0,.55);
  }
  .envelope--warm { top: 101px; }
  .envelope--cool { top: 638px; }

  .brand { position: absolute; left: 56px; top: 56px; display: flex; align-items: center; }
  .brand-square { width: 22px; height: 22px; background: var(--navy); margin-right: 14px; }
  .brand-name {
    font-family: "Source Sans 3", Arial, sans-serif; font-weight: 600;
    font-size: 34px; line-height: 38px; color: var(--ink);
  }
  .brand-tagline {
    position: absolute; left: 92px; top: 100px;
    font-family: "Source Sans 3", Arial, sans-serif; font-weight: 400;
    font-size: 16px; letter-spacing: 1px; color: var(--grey);
  }

  .contact {
    position: absolute; left: 0; right: 0; top: 359px; text-align: center;
    font-size: 17px; color: var(--ink); font-weight: 600;
  }
  .contact-item { margin: 0 10px; }
  .contact-item.email { font-weight: 400; }
  .contact-key { font-weight: 600; }
  .website { display: block; margin-top: 2px; font-size: 18.5px; font-weight: 600; }

  .envelope--warm .contact-key, .envelope--warm .website { color: var(--orange); }
  .envelope--cool .contact-key, .envelope--cool .website { color: var(--sky); }

  .stripe-thin { position: absolute; left: 0; right: 0; top: 416px; height: 6px; }
  .stripe-band { position: absolute; left: 0; right: 0; top: 426px; height: 38px; }
  .envelope--warm .stripe-thin { background: linear-gradient(90deg, var(--orange), var(--amber)); }
  .envelope--warm .stripe-band { background: var(--navy); }
  .envelope--cool .stripe-thin { background: var(--navy); }
  .envelope--cool .stripe-band { background: var(--sky); }
</style>
</head>
<body>

  <div class="option-number" style="top:128px">3</div>
  <section class="envelope envelope--warm">
    <div class="brand">
      <div class="brand-square"></div>
      <div class="brand-name">Brindlemoor Tax Consultancy</div>
    </div>
    <div class="brand-tagline">Specialist tax advisory for accounting practices</div>
    <div class="contact">
      <span class="contact-item"><span class="contact-key">P</span> :902.555.0142</span>
      <span class="contact-item"><span class="contact-key">F</span> :902.555.0187</span>
      <span class="contact-item email"><span class="contact-key">E</span> :nora@brindlemoortax.services</span>
      <span class="website">www.brindlemoortax.services</span>
    </div>
    <div class="stripe-thin"></div>
    <div class="stripe-band"></div>
  </section>

  <div class="option-number" style="top:665px">4</div>
  <section class="envelope envelope--cool">
    <div class="brand">
      <div class="brand-square"></div>
      <div class="brand-name">Brindlemoor Tax Consultancy</div>
    </div>
    <div class="brand-tagline">Specialist tax advisory for accounting practices</div>
    <div class="contact">
      <span class="contact-item"><span class="contact-key">P</span> :902.555.0142</span>
      <span class="contact-item"><span class="contact-key">F</span> :902.555.0187</span>
      <span class="contact-item email"><span class="contact-key">E</span> :nora@brindlemoortax.services</span>
      <span class="website">www.brindlemoortax.services</span>
    </div>
    <div class="stripe-thin"></div>
    <div class="stripe-band"></div>
  </section>

</body>
</html>
```